Flyer
Super tolle Arbeit, Greta hat sich wahnsinnige Mühe gegeben und ein perfektes Ergebnis geliefert. Jederzeit wieder!!!
Zielgruppe
Wir bauen hochwertige Design Esstische aus Holz auch Couchtische und Konferenztische unser Zielgruppe sind Menschen die Wert auch hochwertige Handarbeit legen und denen Design wichtig ist
Aufgabenstellung
Bitte designt einen Flyer, bei den Format bin ich offen, nur keine Spezial Formate die dann beim Drucken teurer sind. Ansonsten sollten Bilder unserer Tische zu sehen sein, außerdem ein Text mit der Beschreibung was wir machen, wofür wir stehen und was uns wichtig ist. Es sollte auch ein Bild von meinem Kollegen und mir zu sehen sein und die Kontaktdaten natürlich. Bilder und Texte könnt ihr der Website entnehmen. Wir stehen für ein minimalistisches und cleanes design und das sollte bei dem Flyer ebenfalls der Fall sein.

```html
<!DOCTYPE html>
<html lang="de">
<head>
<meta charset="utf-8">
<title>Hallmann Manufaktur – Flyer</title>
<link href="https://fonts.googleapis.com/css2?family=Bebas+Neue&family=Montserrat:wght@400;500;600;700&display=swap" rel="stylesheet">
<style>
  :root{
    --brown:#8b5a3b;
    --cream:#f7f4ef;
    --grain:#e6e2dc;
    --ink:#1a1a1a;
    --black:#0c0c0c;
    --white:#ffffff;
    --muted:#555555;
    --stage:#d6d6d6;
  }
  *{box-sizing:border-box;margin:0;padding:0}
  html,body{width:873px;height:1200px;overflow:hidden}
  body{background:var(--stage);font-family:'Montserrat',sans-serif;color:var(--ink);position:relative}
  .page{position:absolute;top:317px;width:400px;height:566px;background:var(--cream);overflow:hidden;box-shadow:0 6px 18px rgba(0,0,0,.25)}
  .page--front{left:24px}
  .page--back{left:449px;background:var(--white)}
  .abs{position:absolute}

  /* front */
  .brand-block{left:0;top:0;width:164px;height:152px;background:var(--white);display:flex;align-items:center;justify-content:center}
  .brand-name{font-size:15px;font-weight:600;line-height:1.25;text-align:center;color:var(--ink)}
  .team-photo{left:164px;top:0;width:236px;height:223px;background:linear-gradient(160deg,#5a4633 0%,#2a2420 45%,#0e0e0e 100%)}
  .headline-band{left:0;top:152px;width:237px;height:71px;background:var(--brown);border-top-right-radius:12px;padding:8px 0 0 32px}
  .headline{font-family:'Bebas Neue',sans-serif;font-weight:400;color:var(--white);font-size:30px;line-height:.86;letter-spacing:.5px}
  .accent-rule{left:0;top:223px;width:400px;height:2px;background:var(--brown)}
  .grain-zone{left:0;top:346px;width:400px;height:184px;background:var(--grain)}
  .welcome{left:0;top:235px;width:400px;text-align:center;font-size:9.4px;line-height:1.3}
  .welcome strong{display:block;font-weight:600;font-size:11px}
  .circle{width:104px;height:104px;border-radius:50%;border:3px solid var(--brown);box-shadow:0 5px 8px rgba(0,0,0,.25)}
  .section-title{font-weight:700;color:var(--brown);font-size:12px;text-transform:uppercase}
  .about-title{left:0;top:416px;width:400px;display:flex;align-items:center;justify-content:center;gap:10px}
  .about-title .section-title{font-size:13px}
  .about-title .rule{width:88px;height:1.5px;background:var(--brown)}
  .about-text{left:32px;top:436px;width:336px;text-align:center;font-size:7.4px;line-height:1.35}
  .web-tab{left:86px;top:527px;width:235px;height:39px;background:var(--black);border-radius:22px 22px 0 0;color:var(--white);font-weight:600;font-size:11px;display:flex;align-items:center;justify-content:center}
  .base-bar{left:0;top:559px;width:400px;height:7px;background:var(--black)}

  /* back */
  .values-zone{left:0;top:0;width:200px;height:252px;background:var(--grain)}
  .wood-photo{left:200px;top:0;width:200px;height:252px;background:radial-gradient(circle at 40% 60%,#d9a85a 0%,#b97f32 45%,#8d8a86 100%)}
  .values{left:36px;top:28px;width:160px}
  .values .section-title,.vision .section-title{line-height:1.05;margin-bottom:4px}
  .copy{font-size:7.3px;line-height:1.35}
  .dining-photo{left:0;top:252px;width:200px;height:218px;background:linear-gradient(180deg,#c8c7c4 0%,#a9a29a 55%,#7a5534 100%);border-bottom-right-radius:18px}
  .vision{left:216px;top:324px;width:170px}
  .handle{left:216px;top:446px;font-size:8px;letter-spacing:.18em;color:var(--muted)}
  .footer{left:0;top:480px;width:400px;height:86px;background:var(--black);color:var(--white)}
  .contacts{left:34px;top:16px;list-style:none;font-size:8.3px;font-weight:600;line-height:1.65}
  .contacts li{display:flex;align-items:center;gap:6px}
  .contacts svg{width:8px;height:8px;fill:var(--white);flex:none}
  .divider{left:226px;top:14px;width:1px;height:50px;background:#777}
  .footer-brand{left:244px;top:24px;font-size:14px;font-weight:600;line-height:1.25;color:var(--white)}
</style>
</head>
<body>

<section class="page page--front">
  <div class="abs brand-block">
    <div class="brand-name">Hallmann<br>Manufaktur</div>
  </div>
  <div class="abs team-photo" role="img" aria-label="Foto der beiden Gründer in der Werkstatt"></div>
  <div class="abs headline-band">
    <h1 class="headline">Tischunikate<br>aus einem Stück</h1>
  </div>
  <div class="abs accent-rule"></div>
  <div class="abs grain-zone" role="img" aria-label="Helle Holzmaserung als Hintergrund"></div>

  <p class="abs welcome"><strong>Willkommen bei der Hallmann Manufaktur.</strong>Wir fertigen hochwertige Monolith-Tische aus einer einzigen Bohle<br>heimischen Holzes! Zeitlos, beständig und mit Liebe zum Detail.</p>

  <div class="abs circle" style="left:40px;top:290px;background:linear-gradient(180deg,#d8d8d8 0%,#b78a55 50%,#5a3421 100%)" role="img" aria-label="Holztisch mit dunklen Kufen"></div>
  <div class="abs circle" style="left:148px;top:290px;background:linear-gradient(180deg,#2a2622 0%,#8a6d50 45%,#767676 100%)" role="img" aria-label="Holztisch mit Glasbeinen in einem Gewölbe"></div>
  <div class="abs circle" style="left:257px;top:290px;background:linear-gradient(180deg,#ffffff 0%,#4a4a4a 30%,#eef2f0 45%,#ffffff 100%)" role="img" aria-label="Tisch mit Glaswangen vor weißem Hintergrund"></div>

  <div class="abs about-title"><span class="rule"></span><h2 class="section-title">Über uns</h2><span class="rule"></span></div>
  <p class="abs about-text">Ich bin Jonas Hallmann und Gründer der Hallmann Manufaktur. Mein Vater war Holzbildhauer, wodurch ich bereits in früher Kindheit mit dem Material Holz in Kontakt kam und seither Techniken der Holzbearbeitung erlernte. Inzwischen habe ich mich mit dem Schreiner Timo Brenner auf die Arbeit mit Holzmonolithen spezialisiert, also die Herstellung von Esstischen die aus einer einzigen großen Bohle geschaffen werden. Darüber hinaus stellen wir leidenschaftlich gerne Couchtische, Waschtischplatten und Konferenztische her.</p>

  <div class="abs base-bar"></div>
  <div class="abs web-tab">www.hallmann-manufaktur.de</div>
</section>

<section class="page page--back">
  <div class="abs values-zone" role="img" aria-label="Helle Holzmaserung als Hintergrund"></div>
  <div class="abs wood-photo" role="img" aria-label="Baumscheiben mit Rissen und schwarzem Harz"></div>
  <div class="abs values">
    <h2 class="section-title">Werte der Hallmann<br>Manufaktur</h2>
    <p class="copy">Unsere Werte bilden das Fundament der Hallmann Manufaktur. Gegenseitiger Respekt, Vertrauen und die Hingabe, die Wünsche unserer Kunden in die Realität umzusetzen, stehen im Mittelpunkt unserer Arbeit. Wir legen höchsten Anspruch an Qualität, verwenden ausschließlich hochwertigste Materialien und setzen auf Regionalität. Mit unserer Arbeit möchten wir nachhaltige Möbel schaffen, die Generationen überdauern und Freude bereiten.</p>
  </div>

  <div class="abs dining-photo" role="img" aria-label="Massivholztisch mit Blumenvase am Fenster"></div>

  <div class="abs circle" style="left:36px;top:196px;background:linear-gradient(180deg,#ffffff 0%,#c89a5e 30%,#e9dcc8 45%,#ffffff 100%)" role="img" aria-label="Tischplatte mit Glasbein, Detail"></div>
  <div class="abs circle" style="left:148px;top:196px;background:linear-gradient(180deg,#ffffff 0%,#d2a461 35%,#efe3d0 55%,#ffffff 100%)" role="img" aria-label="Baumkante einer Tischplatte, Detail"></div>
  <div class="abs circle" style="left:257px;top:196px;background:linear-gradient(180deg,#ffffff 0%,#c4924f 35%,#e6efe9 55%,#ffffff 100%)" role="img" aria-label="Tischecke mit Glaswange, Detail"></div>

  <div class="abs vision">
    <h2 class="section-title">Unsere Vision</h2>
    <p class="copy">Unsere Vision bei der Hallmann Manufaktur ist es, einen Beitrag zu leisten die Möbelbranche nachhaltig zu verändern. Wir möchten Möbel herstellen, die nicht nur von hoher Qualität sind, sondern auch ein Leben lang halten und zum Vererben geeignet sind. Unsere einzigartigen Unikate sollen Wohnräume bereichern und ein zeitloses Design verkörpern.</p>
  </div>
  <div class="abs handle">HALLMANN_MANUFAKTUR</div>

  <footer class="abs footer">
    <ul class="abs contacts">
      <li><svg viewBox="0 0 24 24"><path d="M6.6 10.8a15.2 15.2 0 0 0 6.6 6.6l2.2-2.2a1 1 0 0 1 1-.25 11.4 11.4 0 0 0 3.6.57 1 1 0 0 1 1 1V20a1 1 0 0 1-1 1A17 17 0 0 1 3 4a1 1 0 0 1 1-1h3.5a1 1 0 0 1 1 1c0 1.25.2 2.45.57 3.57a1 1 0 0 1-.25 1z"/></svg>0157/48210093</li>
      <li><svg viewBox="0 0 24 24"><path d="M2 5h20v14H2zm2 2v.5l8 5 8-5V7z"/></svg>hallmann_manufaktur@mail.de</li>
      <li><svg viewBox="0 0 24 24"><circle cx="12" cy="12" r="10"/></svg>www.hallmann-manufaktur.de</li>
      <li><svg viewBox="0 0 24 24"><path d="M12 2a7 7 0 0 0-7 7c0 5.2 7 13 7 13s7-7.8 7-13a7 7 0 0 0-7-7zm0 9.5A2.5 2.5 0 1 1 12 6.5a2.5 2.5 0 0 1 0 5z"/></svg>Lindenweg 18, 70199 Stuttgart</li>
    </ul>
    <div class="abs divider"></div>
    <div class="abs footer-brand">Hallmann<br>Manufaktur</div>
  </footer>
</section>

</body>
</html>
```